Triathlon coaching company website design

A website is needed for a coaching company called StrideVantage. The company provides coaching services to triathletes and other endurance athletes. This includes 1:1 coaching, individualized training plan development, race preparation, and access to guidance and advice on all aspects of developing and maintaining a healthy lifestyle. The design should appeal to all levels of athletes, but be professional in appearance. The tone of the site should be in keeping with the company tagline: Endurance. Resilience. Achievement.

Target Market(s)

All levels of triathletes - beginners to professionals

Industry/Entity Type

It Company

Coding

Coded - Design and coding required

Number of Pages Required

1 page

Colors

Designer to choose colors to be used in the design.

Requirements
Must have
• Pages that should be included must cover: Introductory (Home), description in detail of what we do, description of the main coach (bio) and others types of expert advisors who can be available, link to contact the company, race reports for coaches and athletes that can be regularly updated, links to other sites of potential interest (e.g. other triathlon sites or my facebook page), twitter feed, sign up for email updates. Ability to add other links and pages in future months (e.g. shared calendar access to book meetings, credit card functionality, testimonials)
Should not have
• Not loud or down market feel - target market will largely be highly educated and reasonably affluent

```html
<!DOCTYPE html>
<html lang="en">
<head>
<meta charset="utf-8">
<title>StrideVantage — Triathlon Coaching</title>
<link href="https://fonts.googleapis.com/css2?family=Roboto+Condensed:wght@300;400;700&family=Raleway:wght@400;500&family=Open+Sans:wght@400;600&display=swap" rel="stylesheet">
<style>
:root{
  --red:#b0282c;
  --red-dark:#9c2226;
  --teal:#1f6f6c;
  --amber:#a9652a;
  --green:#3a952f;
  --ink:#222;
  --grey:#7a7a7a;
  --rule:#d8d8d8;
  --footer:#2b2f33;
  --white:#fff;
}
*{margin:0;padding:0;box-sizing:border-box}
html,body{width:1200px;height:2782px;overflow:hidden;background:var(--white)}
body{position:relative;font-family:"Open Sans",sans-serif;color:var(--ink)}
.abs{position:absolute}

/* hero */
.hero{left:0;top:0;width:1200px;height:753px;overflow:hidden}
.hero-photo{left:0;top:0;width:1200px;height:753px;background:radial-gradient(ellipse at 70% 60%,#6d5a3c 0%,#3e3a2c 40%,#23251f 80%),#2a2a24}
.hero-figure{left:760px;top:0;width:400px;height:753px;background:linear-gradient(180deg,rgba(40,110,190,.55) 0%,rgba(60,60,60,.45) 45%,rgba(40,40,40,.3) 100%);border-radius:0 0 40px 40px}
.side-panel{left:0;top:0;width:510px;height:753px;background:rgba(18,18,16,.72)}
.dash{top:0;width:0;height:753px;border-left:1px dashed rgba(255,255,255,.6)}
.brand{left:85px;top:124px;font-family:"Roboto Condensed",sans-serif;font-weight:700;font-size:44px;color:var(--red);letter-spacing:-.5px}
.nav{left:85px;top:292px;width:305px;list-style:none}
.nav li{height:42.5px;display:flex;align-items:center;font-family:"Roboto Condensed",sans-serif;font-size:17px;color:var(--white);text-transform:uppercase}
.nav li::after{content:"";flex:1;height:1px;background:rgba(255,255,255,.35);margin-left:14px}
.social{top:612px;width:22px;height:22px;border-radius:50%;background:var(--white)}
.hero-copy{left:553px;top:258px;width:600px;text-align:center;color:var(--white)}
.hero-kicker{font-family:"Raleway",sans-serif;font-size:27px;letter-spacing:1px}
.hero-kicker b{font-weight:700;font-family:"Roboto Condensed",sans-serif;font-size:29px}
.hero-name{font-family:"Raleway",sans-serif;font-size:46px;letter-spacing:1px;margin-top:6px}
.hero-rule{width:460px;height:2px;background:var(--red);margin:10px auto 0}
.hero-tag{font-family:"Raleway",sans-serif;font-size:25px;letter-spacing:2px;margin-top:20px}
.btn{display:flex;align-items:center;justify-content:center;background:var(--red);color:var(--white);font-family:"Raleway",sans-serif;border-radius:30px;text-transform:uppercase}
.hero-btn{left:728px;top:491px;width:250px;height:60px;font-size:22px}
.dot{left:1171px;width:10px;height:10px;border-radius:50%;background:var(--white)}

/* services */
.tile{top:785px;width:236px;height:183px;color:var(--white);text-align:center;font-family:"Roboto Condensed",sans-serif;font-weight:700;font-size:19px;line-height:24px}
.tile .ring{position:absolute;left:87px;top:22px;width:62px;height:62px;border:2px solid var(--white);border-radius:50%;display:flex;align-items:center;justify-content:center}
.tile .label{position:absolute;left:0;right:0;top:120px}
.t1{left:85px;background:var(--red)}
.t2{left:349px;background:var(--teal)}
.t3{left:612px;background:var(--amber)}
.t4{left:876px;background:var(--green)}
.chev{top:856px}

/* about */
.section-title{font-family:"Roboto Condensed",sans-serif;font-weight:300;font-size:46px;color:var(--ink);letter-spacing:1px}
.section-title b{font-weight:700}
.about-title{left:0;top:1068px;width:1200px;display:flex;align-items:center;justify-content:center}
.about-title::before,.about-title::after{content:"";width:290px;height:1px;background:var(--rule);margin:0 14px}
.about-text{left:85px;top:1160px;width:1028px;text-align:center;font-size:14.6px;line-height:24.8px;color:var(--grey)}
.about-btn{left:481px;top:1372px;width:226px;height:56px;font-size:19px}

/* testimonial */
.quote-band{left:0;top:1582px;width:1200px;height:195px;background:var(--red);color:var(--white);text-align:center}
.quote-text{position:absolute;left:100px;right:100px;top:72px;font-family:"Roboto Condensed",sans-serif;font-size:16.5px;line-height:27px}
.quote-by{position:absolute;left:0;right:0;top:146px;font-family:"Roboto Condensed",sans-serif;font-size:15px}
.quote-by b{font-weight:700}
.quote-by i{font-weight:300}
.avatar{left:529px;top:1509px;width:136px;height:136px;border-radius:50%;border:5px solid var(--white);background:linear-gradient(180deg,#b9d4e6 0%,#6f7f88 60%,#3d4448 100%)}

/* coach */
.coach-photo{left:85px;top:1888px;width:412px;height:382px;background:radial-gradient(ellipse at 55% 40%,#6e6e6e 0%,#3a3a3a 55%,#1c1c1c 100%)}
.coach-title{left:582px;top:1895px}
.coach-rule{left:586px;top:1978px;width:490px;height:1px;background:var(--rule)}
.coach-tick{left:586px;top:1966px;width:1px;height:24px;background:var(--rule)}
.coach-text{left:582px;top:2014px;width:540px;font-size:13.3px;line-height:25.5px;color:var(--grey)}
.coach-btn{left:586px;top:2222px;width:271px;height:56px;font-size:19px}

/* footer */
.footer{left:0;top:2389px;width:1200px;height:345px;background:var(--footer);color:var(--white);font-family:"Roboto Condensed",sans-serif}
.f-brand{position:absolute;left:139px;top:72px;font-weight:700;font-size:34px;color:var(--red)}
.f-about{position:absolute;left:139px;top:146px;width:260px;font-size:13.5px;line-height:23px;color:#b5b5b5}
.f-contact{position:absolute;left:139px;font-size:14px;display:flex;align-items:center;gap:12px}
.f-head{position:absolute;font-size:14px;text-transform:uppercase;letter-spacing:.3px}
.f-head::after{content:"";display:block;width:44px;height:1px;background:var(--red);margin-top:6px}
.post{position:absolute;left:514px;width:220px}
.post-title{font-size:13.5px}
.post-date{font-size:10.5px;color:#a8a8a8;margin-top:8px}
.post-ex{font-size:11.5px;line-height:22px;margin-top:5px}
.f-input{position:absolute;left:846px;top:108px;width:146px;height:37px;border:1px solid #8a8d90;font-size:12px;color:#9a9a9a;padding:10px 12px}
.f-go{position:absolute;left:998px;top:108px;width:56px;height:37px;background:var(--red);display:flex;align-items:center;justify-content:center;font-weight:700;font-size:17px}
.f-social{position:absolute;top:228px;width:20px;height:20px;border-radius:50%;background:var(--white)}
.copyright{left:0;top:2734px;width:1200px;height:48px;background:var(--red);color:var(--white);display:flex;align-items:center;justify-content:center;font-size:11.5px}
</style>
</head>
<body>

<header class="abs hero">
  <div class="abs hero-photo" role="img" aria-label="Photograph of an athlete stretching on a forest trail before a run"></div>
  <div class="abs hero-figure" aria-hidden="true"></div>
  <div class="abs side-panel"></div>
  <div class="abs dash" style="left:553px"></div>
  <div class="abs dash" style="left:1152px"></div>

  <div class="abs brand">StrideVantage</div>

  <ul class="abs nav">
    <li>Home</li>
    <li>Our Services</li>
    <li>Bio</li>
    <li>Expert Advisors</li>
    <li>Race Reports</li>
    <li>Contact Us</li>
  </ul>

  <span class="abs social" style="left:148px" aria-label="Social link 1"></span>
  <span class="abs social" style="left:198px" aria-label="Social link 2"></span>
  <span class="abs social" style="left:250px" aria-label="Social link 3"></span>
  <span class="abs social" style="left:301px" aria-label="Social link 4"></span>

  <div class="abs hero-copy">
    <div class="hero-kicker"><b>TRIATHLON</b> WITH</div>
    <div class="hero-name">MARCUS HALE</div>
    <div class="hero-rule"></div>
    <div class="hero-tag">Endurance. Resilience. Achievement</div>
  </div>
  <a class="abs btn hero-btn">Contact Us</a>

  <span class="abs dot" style="top:357px;background:var(--red)"></span>
  <span class="abs dot" style="top:381px"></span>
  <span class="abs dot" style="top:403px"></span>
</header>

<svg class="abs chev" style="left:28px" width="20" height="46" viewBox="0 0 20 46"><polyline points="18,2 2,23 18,44" fill="none" stroke="#ccc" stroke-width="2"/></svg>
<svg class="abs chev" style="left:1144px" width="20" height="46" viewBox="0 0 20 46"><polyline points="2,2 18,23 2,44" fill="none" stroke="#ccc" stroke-width="2"/></svg>

<section>
  <div class="abs tile t1">
    <span class="ring"><svg width="34" height="30" viewBox="0 0 34 30" fill="#fff"><circle cx="8" cy="14" r="3.5"/><circle cx="17" cy="14" r="3.5"/><circle cx="26" cy="14" r="3.5"/><path d="M2 27c0-5 12-5 12 0zM11 27c0-5 12-5 12 0zM20 27c0-5 12-5 12 0z"/><rect x="18" y="0" width="12" height="8" rx="2"/></svg></span>
    <span class="label">1:1 COACHING</span>
  </div>
  <div class="abs tile t2">
    <span class="ring"><svg width="30" height="30" viewBox="0 0 30 30" fill="none" stroke="#fff" stroke-width="2.4"><rect x="4" y="6" width="22" height="20" rx="2"/><line x1="9" y1="2" x2="9" y2="9"/><line x1="21" y1="2" x2="21" y2="9"/><g fill="#fff" stroke="none"><rect x="8" y="13" width="4" height="3"/><rect x="13" y="13" width="4" height="3"/><rect x="18" y="13" width="4" height="3"/><rect x="8" y="19" width="4" height="3"/><rect x="13" y="19" width="4" height="3"/><rect x="18" y="19" width="4" height="3"/></g></svg></span>
    <span class="label">TRAINING PLAN<br>DEVELOPMENT</span>
  </div>
  <div class="abs tile t3">
    <span class="ring"><svg width="32" height="32" viewBox="0 0 32 32" fill="#fff"><circle cx="16" cy="13" r="8"/><path d="M5 30c0-7 22-7 22 0z"/><path d="M6 14a10 10 0 0 1 20 0" fill="none" stroke="#fff" stroke-width="2.4"/><rect x="4" y="12" width="4" height="7" rx="1.5"/><rect x="24" y="12" width="4" height="7" rx="1.5"/></svg></span>
    <span class="label">CONSULTATION</span>
  </div>
  <div class="abs tile t4">
    <span class="ring"><svg width="30" height="32" viewBox="0 0 30 32" fill="none" stroke="#fff" stroke-width="2.4" stroke-linecap="round"><circle cx="14" cy="5" r="3" fill="#fff" stroke="none"/><path d="M14 10v10l-4 10M14 20l5 10M8 12l6 2 6-6"/><circle cx="24" cy="5" r="4"/></svg></span>
    <span class="label">LIFESTYLE COACHING</span>
  </div>
</section>

<section>
  <h2 class="abs section-title about-title">ABOUT&nbsp;<b>STRIDEVANTAGE</b></h2>
  <p class="abs about-text">At StrideVantage we believe that everyone has a unique set of circumstances, motivations and abilities that need to be taken into consideration in developing their program. Defining success is personal, as is the path to achieving that success. Every person has their own goals: for some it is about health and wellness, for others the focus is lifestyle, and in other cases specific competitive goals are the target. So we focus on understanding you as an individual athlete in the context of your wider life - your goals, your training history, your physiology and psychology as well as other aspects of your life. The foundation of any program should be based on objective data and facts, overlaid with personal experience and circumstance. Given the right approach we strive to help athletes of all types and levels improve endurance, increase their resilience in the face of challenges, and develop a powerful sense of achievement. Endurance, Resilience, Achievement are the watch-words of the StrideVantage brand.</p>
  <a class="abs btn about-btn">Contact Us</a>
</section>

<section>
  <div class="abs quote-band">
    <p class="quote-text">An entity which provides insurance is known as an insurer, insurance company, or insurance carrier. A person or entity who buys insurance is known as an insured or policyholder. The action involves a contract.</p>
    <p class="quote-by"><b>DAN KELLER</b>, <i>Athlete</i></p>
  </div>
  <div class="abs avatar" role="img" aria-label="Portrait photograph of an athlete"></div>
</section>

<section>
  <div class="abs coach-photo" role="img" aria-label="Portrait photograph of the head coach holding a clipboard"></div>
  <h2 class="abs section-title coach-title">ABOUT <b>MARCUS HALE</b></h2>
  <div class="abs coach-tick"></div>
  <div class="abs coach-rule"></div>
  <p class="abs coach-text">Triathlon is my passion which, in the past, coexisted with my day job as a management consultant - so I absolutely understand the challenges of fitting triathlon into a busy work, family and social life. I started competing in endurance sports in my teens as a rower, ultimately competing for Great Britain at the World Championships, and have continued as an endurance athlete throughout my life. My first triathlon was an Olympic distance event in Japan in 2001, which sparked my interest in the complexities and and rewards of multi-sport and long distance racing.</p>
  <a class="abs btn coach-btn">View Other Coaches</a>
</section>

<footer class="abs footer">
  <div class="f-brand">StrideVantage</div>
  <p class="f-about">Lorem Ipsum is simply dummy text of the printing and typesetting industry.</p>
  <div class="f-contact" style="top:229px"><svg width="12" height="12" viewBox="0 0 12 12"><path d="M2 1l2.5 0 1 3-1.5 1a7 7 0 0 0 3 3l1-1.5 3 1V10a1 1 0 0 1-1 1C5 11 1 7 1 2a1 1 0 0 1 1-1z" fill="var(--red)"/></svg>(555) 014-2290</div>
  <div class="f-contact" style="top:259px"><svg width="12" height="10" viewBox="0 0 12 10"><rect x="0" y="0" width="12" height="10" rx="1" fill="var(--red)"/><polyline points="0,1 6,6 12,1" fill="none" stroke="var(--footer)" stroke-width="1.2"/></svg>marcus.hale@stridevantage.com</div>

  <div class="f-head" style="left:514px;top:58px">Recent Blog Posts</div>
  <div class="post" style="top:98px">
    <div class="post-title">Nulla consequat massa quis enim</div>
    <div class="post-date">November 19, 2016</div>
    <div class="post-ex">The sight of the tumblers restored Bob Sawyer …</div>
  </div>
  <div class="post" style="top:216px">
    <div class="post-title">Nulla consequat massa quis enim</div>
    <div class="post-date">November 19, 2016</div>
    <div class="post-ex">The sight of the tumblers restored Bob Sawyer to …</div>
  </div>

  <div class="f-head" style="left:844px;top:58px">Newsletter</div>
  <div class="f-input">Your Email Id...</div>
  <div class="f-go">GO</div>
  <div class="f-head" style="left:844px;top:180px">Follow Us</div>
  <span class="f-social" style="left:849px" aria-label="Social link 1"></span>
  <span class="f-social" style="left:901px" aria-label="Social link 2"></span>
  <span class="f-social" style="left:951px" aria-label="Social link 3"></span>
  <span class="f-social" style="left:1005px" aria-label="Social link 4"></span>
</footer>

<div class="abs copyright">stridevantage.com2017. All rights reserved</div>

</body>
</html>
```